Website Design For Atelier Nine Design Group

Create a sophisticated website that denotes high-end luxury. We would like to keep the copy minimalist and elegantly understated while communicating only the most essential information. While creating an air of exclusivity.
We would like 3-4 Tab Wesbite
Home:
• Feature a design project front and centre, along with a short
introduction about who we are and what we do.

We can put a Call To Action at the end of the introduction inviting readers to learn more on our About page.
About:
• This page should provide more detail on our background, past
achievements, history of the company, and anything you'd like to
highlight.
• We should also provide details on our services, aesthetic, process, etc.
Team:
• introduce the team, possibly with short descriptions for each
team member. Total Team Members 7
Residential
• The portfolio page can be a grid of images along with titles for
each project.
• Clicking on each image should take you to a separate page for that
project where readers can find more details

Commercial
The portfolio page can be a grid of images along with titles for
each project.

Contact Us:

example website:
https://www.venkorahinteriors.example/

Target Market(s)

High end luxury clientele

Industry/Entity Type

Interior Design

Number of Pages Required

4 page

Font styles to use
Sans Serif

Requirements
Must have
• Company logo, color scheme and name: Atelier Nine Design Group

```html
<!DOCTYPE html>
<html lang="en">
<head>
<meta charset="utf-8">
<title>Atelier Nine Design Group</title>
<link href="https://fonts.googleapis.com/css2?family=Cormorant+Garamond:wght@500;600;700&family=Nunito+Sans:wght@400;600&display=swap" rel="stylesheet">
<style>
:root{
  --green:#114a3c;
  --gold:#c6a04a;
  --teal:#07333f;
  --grey:#f3f3f3;
  --ink:#2b2b2b;
  --white:#ffffff;
}
*{margin:0;padding:0;box-sizing:border-box}
html,body{width:1200px;height:3649px;overflow:hidden}
body{position:relative;background:var(--white);font-family:"Nunito Sans",sans-serif;color:var(--ink)}
.abs{position:absolute}
.serif{font-family:"Cormorant Garamond",serif}
.center{text-align:center}

/* header */
.site-header{left:0;top:0;width:1200px;height:128px;border-bottom:3px solid var(--gold)}
.main-nav{left:92px;top:57px;display:flex;gap:17px;font-size:12px;font-weight:600;color:#111;letter-spacing:.2px}
.main-nav .active{color:var(--gold)}
.brand{left:450px;top:18px;width:300px;display:flex;flex-direction:column;align-items:center;gap:8px}
.brand-mark{width:22px;height:22px;border:2.5px solid var(--teal)}
.brand-name{font-size:23px;font-weight:600;color:var(--teal);letter-spacing:3px;line-height:26px}
.social{left:934px;top:56px;display:flex;gap:16px}
.social span{width:16px;height:16px;border-radius:50%;border:2px solid #555}
.menu-dots{left:1049px;top:56px;width:18px;height:18px;display:grid;grid-template-columns:repeat(3,4px);gap:3px}
.menu-dots i{width:4px;height:4px;background:var(--gold);border-radius:50%}

/* hero */
.hero-photo{top:130px;height:595px}
.hero-bath{left:0;width:400px;background:
  radial-gradient(ellipse 55% 30% at 30% 72%,#f4f4f3 0%,rgba(244,244,243,0) 70%),
  radial-gradient(ellipse 18% 22% at 18% 88%,#6e6a64 0%,rgba(110,106,100,0) 75%),
  linear-gradient(180deg,#a6a7a9 0%,#8f9193 40%,#b9b6b1 60%,#8d8a86 100%)}
.hero-living{left:400px;width:400px;background:
  radial-gradient(ellipse 22% 14% at 55% 8%,#a98b62 0%,rgba(169,139,98,0) 80%),
  radial-gradient(ellipse 35% 45% at 70% 55%,#dad6cc 0%,rgba(218,214,204,0) 75%),
  linear-gradient(90deg,#2f4a3c 0%,#3b5547 30%,#8d8b83 55%,#b8b3aa 75%,#3c5446 100%)}
.hero-study{left:800px;width:400px;height:597px;background:
  radial-gradient(ellipse 30% 35% at 82% 70%,#cfc8bd 0%,rgba(207,200,189,0) 75%),
  radial-gradient(ellipse 45% 22% at 40% 65%,#3a3836 0%,rgba(58,56,54,0) 80%),
  linear-gradient(180deg,#3d4a48 0%,#5d6360 35%,#d9d4c9 52%,#8f8d88 70%,#9ea5ae 100%)}
.hero-title{left:0;top:335px;width:1200px;color:var(--white);font-size:35px;letter-spacing:5px;line-height:42px;font-weight:500;text-shadow:0 1px 6px rgba(0,0,0,.25)}

/* welcome */
.welcome{left:187px;top:629px;width:829px;height:370px;border:2px solid var(--gold);background:var(--white)}
.welcome h2{margin-top:60px;font-size:34px;letter-spacing:5px;color:var(--green);font-weight:600}
.welcome p{width:505px;margin:32px auto 0;font-size:12.5px;line-height:22.6px;color:#555}
.btn{display:block;border:1.5px solid var(--gold);color:var(--gold);font-family:"Cormorant Garamond",serif;font-weight:700;font-size:13px;letter-spacing:2.5px;text-align:center}
.welcome .btn{width:157px;height:36px;line-height:33px;margin:26px auto 0}

/* listen */
.listen-art{left:60px;top:965px;width:560px;height:520px;background:radial-gradient(ellipse at center,#fbf6ea 0%,#ffffff 70%)}
.listen-title{left:203px;top:1110px;font-size:28px;line-height:42px;color:var(--green);font-weight:600}
.listen-text{left:202px;top:1262px;width:350px;font-size:13px;line-height:22.6px;color:#666}
.arrows{left:205px;top:1393px;width:74px;height:35px;border:1.5px solid var(--gold);display:flex}
.arrows span{flex:1;display:flex;align-items:center;justify-content:center}
.arrows span+span{border-left:1.5px solid var(--gold)}
.listen-room{left:660px;top:1067px;width:340px;height:371px;background:
  radial-gradient(ellipse 40% 18% at 62% 72%,#e8e4dd 0%,rgba(232,228,221,0) 80%),
  radial-gradient(ellipse 18% 9% at 38% 82%,#2d2b29 0%,rgba(45,43,41,0) 80%),
  linear-gradient(90deg,#2a2a2a 0%,#dfe2e4 12%,#f1f0ee 40%,#e6e4e0 100%)}
.listen-wall{left:1000px;top:1067px;width:200px;height:371px;background:
  radial-gradient(ellipse 25% 20% at 75% 50%,#6c7d4c 0%,rgba(108,125,76,0) 80%),
  linear-gradient(180deg,#8f8f8e 0%,#a3a3a1 50%,#6f655a 70%,#a98063 85%,#8a6b50 100%)}

/* stats band */
.grey-band{left:0;top:1597px;width:1200px;height:904px;background:var(--grey)}
.stat{top:1536px;width:193px;height:193px;background:var(--teal);border:1.5px solid var(--gold);color:var(--white)}
.stat b{display:block;margin-top:55px;font-family:"Cormorant Garamond",serif;font-size:56px;line-height:56px;color:var(--gold);font-weight:600}
.stat small{display:block;margin-top:4px;font-size:13px}
.cta-title{left:0;width:1200px;font-size:21px;font-weight:700;color:var(--green)}
.cta-btn{width:156px;height:35px;line-height:32px}

.section-title{left:0;width:1200px;font-size:32px;letter-spacing:5px;color:var(--green);font-weight:600}
.rule{height:3px;background:var(--gold)}

.service-label{width:300px;font-size:17px;color:#222;font-weight:600}

/* portfolio */
.portfolio-item{top:2681px;width:286px;height:286px}
.pf-lounge{left:140px;background:
  radial-gradient(ellipse 20% 14% at 45% 30%,#f2efe9 0%,rgba(242,239,233,0) 80%),
  radial-gradient(ellipse 45% 12% at 50% 78%,#b4a697 0%,rgba(180,166,151,0) 80%),
  linear-gradient(180deg,#e6e3de 0%,#9d958b 30%,#4b423b 55%,#6f655c 80%,#1d1b1a 100%)}
.pf-hall{left:445px;background:
  radial-gradient(ellipse 25% 18% at 50% 20%,#e6d7b6 0%,rgba(230,215,182,0) 80%),
  radial-gradient(ellipse 50% 18% at 50% 82%,#b8a58d 0%,rgba(184,165,141,0) 80%),
  linear-gradient(180deg,#d8cfbf 0%,#b7aa95 45%,#7b6a58 75%,#5a4a3e 100%)}
.pf-bedroom{left:748px;background:
  radial-gradient(ellipse 35% 14% at 40% 72%,#efe6d6 0%,rgba(239,230,214,0) 80%),
  radial-gradient(ellipse 30% 20% at 50% 15%,#faf8f3 0%,rgba(250,248,243,0) 80%),
  linear-gradient(180deg,#e9e6e0 0%,#cfc4b2 45%,#9d8e7a 75%,#7d7266 100%)}
.portfolio-overlay{left:445px;top:2681px;width:286px;height:286px;background:rgba(20,20,20,.45);color:var(--white)}
.portfolio-overlay .kind{margin-top:117px;font-size:11px}
.portfolio-overlay .name{font-size:16px;letter-spacing:.5px}
.portfolio-overlay .detail{width:111px;height:25px;line-height:22px;margin:14px auto 0;border:1px solid var(--white);font-size:12px}

.hairline{height:1px;background:var(--gold)}
.quote{left:262px;top:3184px;width:676px;font-size:12.5px;line-height:21.5px;color:#222}
.quote .thanks{margin-top:21px}

/* footer */
.site-footer{left:0;top:3572px;width:1200px;height:77px;background:var(--teal);color:var(--white);font-size:12.5px}
.copyright{left:186px;top:32px}
.contact-line{top:30px;display:flex;align-items:center;gap:8px}
</style>
</head>
<body>

<header class="site-header abs">
  <nav class="main-nav abs">
    <span class="active">HOME</span><span>ABOUT</span><span>COMMERCIAL</span><span>CONTACT US</span>
  </nav>
  <div class="brand abs"><span class="brand-mark"></span><span class="brand-name">ATELIER NINE</span></div>
  <div class="social abs" aria-label="Social links"><span></span><span></span><span></span></div>
  <div class="menu-dots abs"><i></i><i></i><i></i><i></i><i></i><i></i><i></i><i></i><i></i></div>
</header>

<section class="hero">
  <div class="hero-photo hero-bath abs" role="img" aria-label="Grey marble bathroom with freestanding tub"></div>
  <div class="hero-photo hero-living abs" role="img" aria-label="Living room with green walls, pendant lamp and patterned curtains"></div>
  <div class="hero-photo hero-study abs" role="img" aria-label="Study with shelving, desk and upholstered armchair"></div>
  <h1 class="hero-title abs serif center">INTERIOR DESIGN COMPANY:<br>QUALITY &amp; LUXURY DESIGN</h1>
</section>

<section class="welcome abs center">
  <h2 class="serif">WELCOME TO ATELIER NINE</h2>
  <p>Lorem ipsum dolor sit amet, consectetur adipiscing elit. Vitae risus gravida porta amet in scelerisque in amet phasellus. Leo egestas dignissim et elit at dolor. Iaculis eget libero morbi velit at. Est magna leo dui, mattis mauris integer. Quis elementum sit tristique pellentesque orci venenatis, at facilisi. Amet at massa mattis in dictum orci facilisis sed condimentum. Est curabitur eget erat ac diam donec et, diam. Lacinia tincidunt eu volutpat gravida enim diam purus lacus. Nulla vehicula.</p>
  <span class="btn">READ MORE</span>
</section>

<section class="listen">
  <div class="listen-art abs" role="img" aria-label="Faint gold line sketch of an interior"></div>
  <h2 class="listen-title abs serif">WE LISTEN, WE<br>UNDERSTAND,<br>WE DESIGN</h2>
  <p class="listen-text abs">Lorem ipsum dolor sit amet, consectetur adipiscing elit. Vitae risus gravida porta amet in scelerisque in amet phasellus. Leo egestas dignissim et elit at dolor. Iaculis eget libero morbi velit at. Est magna leo dui, mattis mauris integer.</p>
  <div class="arrows abs">
    <span><svg width="14" height="10" viewBox="0 0 14 10"><path d="M13 5H1M5 1L1 5l4 4" fill="none" stroke="#c6a04a" stroke-width="1.2"/></svg></span>
    <span><svg width="14" height="10" viewBox="0 0 14 10"><path d="M1 5h12M9 1l4 4-4 4" fill="none" stroke="#c6a04a" stroke-width="1.2"/></svg></span>
  </div>
  <div class="listen-room abs" role="img" aria-label="Bright living room with sofa and round coffee table"></div>
  <div class="listen-wall abs" role="img" aria-label="Concrete feature wall with plant and wooden floor"></div>
</section>

<div class="grey-band abs"></div>

<section class="stats">
  <div class="stat abs center" style="left:261px"><b>28</b><small>Awesome Project</small></div>
  <div class="stat abs center" style="left:503px"><b>30</b><small>Happy Clients</small></div>
  <div class="stat abs center" style="left:745px"><b>32</b><small>Project Finished</small></div>
  <h3 class="cta-title abs serif center" style="top:1796px">Contact Us For A Free Consultation</h3>
  <span class="btn cta-btn abs" style="left:538px;top:1848px">GET IN TOUCH</span>
</section>

<section class="services">
  <h2 class="section-title abs serif center" style="top:1950px">WHAT WE DO</h2>
  <div class="rule abs" style="left:572px;top:1996px;width:54px"></div>
  <svg class="abs" style="left:203px;top:2047px" width="224" height="256" viewBox="0 0 224 256" role="img" aria-label="Pencil sketch of a living room">
    <defs>
      <linearGradient id="hexA" x1="0" y1="0" x2="0" y2="1"><stop offset="0" stop-color="#f6f6f6"/><stop offset=".45" stop-color="#dcdedd"/><stop offset=".7" stop-color="#c5d3cf"/><stop offset="1" stop-color="#f2f2f2"/></linearGradient>
    </defs>
    <polygon points="112,2 222,65 222,191 112,254 2,191 2,65" fill="url(#hexA)" stroke="#c6a04a" stroke-width="2"/>
  </svg>
  <svg class="abs" style="left:507px;top:2037px" width="224" height="256" viewBox="0 0 224 256" role="img" aria-label="Living room with sectional sofa">
    <defs>
      <linearGradient id="hexB" x1="0" y1="0" x2="0" y2="1"><stop offset="0" stop-color="#f2f2f0"/><stop offset=".5" stop-color="#e0ddd8"/><stop offset=".75" stop-color="#c3bcb2"/><stop offset="1" stop-color="#8f8880"/></linearGradient>
    </defs>
    <polygon points="112,2 222,65 222,191 112,254 2,191 2,65" fill="url(#hexB)" stroke="#c6a04a" stroke-width="2"/>
  </svg>
  <svg class="abs" style="left:792px;top:2040px" width="224" height="256" viewBox="0 0 224 256" role="img" aria-label="Bathroom with tub facing a garden">
    <defs>
      <linearGradient id="hexC" x1="0" y1="0" x2="0" y2="1"><stop offset="0" stop-color="#e9ecdf"/><stop offset=".3" stop-color="#6d8a4f"/><stop offset=".55" stop-color="#8aa26a"/><stop offset=".75" stop-color="#efeae2"/><stop offset="1" stop-color="#d9cfc3"/></linearGradient>
    </defs>
    <polygon points="112,2 222,65 222,191 112,254 2,191 2,65" fill="url(#hexC)" stroke="#c6a04a" stroke-width="2"/>
  </svg>
  <p class="service-label abs serif center" style="left:165px;top:2323px">Interior Architecture</p>
  <p class="service-label abs serif center" style="left:469px;top:2323px">Design Project Management</p>
  <p class="service-label abs serif center" style="left:754px;top:2318px">Procurement</p>
</section>

<section class="portfolio">
  <h2 class="section-title abs serif center" style="top:2561px">PORTFOLIO</h2>
  <div class="rule abs" style="left:562px;top:2621px;width:54px"></div>
  <div class="portfolio-item pf-lounge abs" role="img" aria-label="Double-height lounge with ring chandelier"></div>
  <div class="portfolio-item pf-hall abs" role="img" aria-label="Classic hall with crystal chandelier"></div>
  <div class="portfolio-overlay abs center">
    <p class="kind">Commercial</p>
    <p class="name">House of Mr. Hollis</p>
    <p class="detail">Detail</p>
  </div>
  <div class="portfolio-item pf-bedroom abs" role="img" aria-label="Bedroom with upholstered bed and chandelier"></div>
</section>

<div class="hairline abs" style="left:177px;top:3035px;width:843px"></div>

<section class="testimonial">
  <h2 class="section-title abs serif center" style="top:3092px">TESTIMONIAL</h2>
  <div class="rule abs" style="left:576px;top:3137px;width:54px"></div>
  <svg class="abs" style="left:164px;top:3191px" width="12" height="20" viewBox="0 0 12 20"><path d="M10 1L2 10l8 9" fill="none" stroke="#222" stroke-width="1.6"/></svg>
  <svg class="abs" style="left:1027px;top:3200px" width="12" height="20" viewBox="0 0 12 20"><path d="M2 1l8 9-8 9" fill="none" stroke="#222" stroke-width="1.6"/></svg>
  <div class="quote abs center">
    <p>We had a smooth and pleasant renovation journey with Atelier Nine, despite the challenges during the pandemic. We appreciated the advice and ideas shared in the design phase, regular &amp; detailed updates on the actual renovation works, and high standards of quality &amp; workmanship.</p>
    <p class="thanks">Thanks to the team at Atelier Nine</p>
  </div>
</section>

<div class="hairline abs" style="left:171px;top:3364px;width:844px"></div>

<section class="closing-cta">
  <h3 class="cta-title abs serif center" style="top:3416px">Contact Us For A Free Consultation</h3>
  <span class="btn cta-btn abs" style="left:546px;top:3466px">GET IN TOUCH</span>
</section>

<footer class="site-footer abs">
  <p class="copyright abs">Copyright © Atelier Nine All Rights Reserved</p>
  <div class="contact-line abs" style="left:717px">
    <svg width="18" height="13" viewBox="0 0 18 13"><rect x="1" y="1" width="16" height="11" fill="none" stroke="#c6a04a" stroke-width="1.4"/><path d="M1 1l8 6 8-6" fill="none" stroke="#c6a04a" stroke-width="1.4"/></svg>
    <span>info@ateliernine.co</span>
  </div>
  <div class="contact-line abs" style="left:910px">
    <svg width="17" height="17" viewBox="0 0 24 24"><path d="M5 2h4l2 5-3 2a12 12 0 0 0 7 7l2-3 5 2v4a2 2 0 0 1-2 2A19 19 0 0 1 3 4a2 2 0 0 1 2-2z" fill="none" stroke="#c6a04a" stroke-width="1.6"/></svg>
    <span>555 014 2290</span>
  </div>
</footer>

</body>
</html>
```